Food Safety 1-California workers only

3.25" by 4.5" Black and White Magazine Ad
This ad is to train California workers only.
Workers will be trained on: Food Safety, FSMA (Food Safety Modernization Act), using equipment safety, food processing production skills, worker safety, supervisory skills, communication skills.
"FREE TRAINING", The company does the training or Keystone Learning will provide the training.
Training grants range from $100,000 to $400,000.
Companies must be in business for profit.
Companies must train 200 employees or more.
This program is for California workers only.
Incumbent or new-hires are eligible.

Target Market(s)

California food processors, farms, food packaging, food processors, companies under FSMA, food safety, food production who need to train employees.

Industry/Entity Type

Food Production

Font styles to use
Serif
Sans Serif

Colors

Designer to choose colors to be used in the design.

Requirements
Must have
• This is a 3.25 inch by 4.5 inch magazine ad. It must be black and white. No color.
• The deliverable must be in basic PhotoShop. The ad does not need to include any graphics and be text only if needed. If you have a black and white graphic that will show well.
• Look at www.KLGFoodSafety..com
• Use the text from "MEALBOX-Photoshop-052018" file as your starting point.
Nice to have
• A black and white graphic about food. See www.KLGFoodSafety.com
Should not have
• No color.

```html
<!DOCTYPE html>
<html lang="en">
<head>
<meta charset="utf-8">
<title>Keystone Learning – California Training Ad</title>
<link rel="stylesheet" href="https://fonts.googleapis.com/css2?family=Jost:wght@400;500;700;800&display=swap">
<style>
  :root {
    --backdrop: #a6a7a9;
    --paper: #ffffff;
    --ink: #000000;
    --ink-soft: #2b2b2b;
  }
  * { margin: 0; padding: 0; box-sizing: border-box; }
  html, body { width: 909px; height: 1200px; overflow: hidden; }
  body {
    background: var(--backdrop);
    font-family: "Jost", "Futura", sans-serif;
    position: relative;
  }
  .ad {
    position: absolute;
    left: 135px; top: 157px;
    width: 640px; height: 886px;
    background: var(--paper);
    overflow: hidden;
    color: var(--ink);
    text-transform: uppercase;
  }
  .state-map {
    position: absolute;
    left: 285px; top: 0;
    width: 200px; height: 465px;
    background: var(--ink);
  }
  .state-map-body {
    position: absolute;
    left: 285px; top: 180px;
    width: 270px; height: 285px;
    background: var(--ink);
  }
  .topics {
    position: absolute;
    left: 323px; top: 0;
    width: 317px; height: 180px;
    background: var(--paper);
    padding: 26px 0 0 34px;
    font-size: 38px;
    line-height: 30px;
    color: var(--ink-soft);
    font-weight: 400;
  }
  .topics strong { font-weight: 700; color: var(--ink-soft); display: block; }
  .topics-bar {
    position: absolute;
    left: 540px; top: 120px;
    width: 100px; height: 55px;
    background: var(--ink);
  }
  .pitch {
    position: absolute;
    left: 33px; top: 196px;
    font-size: 40px;
    line-height: 32px;
    color: var(--ink-soft);
    font-weight: 400;
  }
  .pitch strong { display: block; font-weight: 700; }
  .qualify {
    position: absolute;
    left: 0; top: 465px;
    width: 640px; height: 236px;
    background: var(--ink);
    color: var(--paper);
    padding: 16px 0 0 31px;
  }
  .qualify h2 { font-size: 19px; font-weight: 700; margin-bottom: 10px; letter-spacing: .3px; }
  .qualify ul { list-style: none; font-size: 20px; line-height: 26px; font-weight: 400; }
  .qualify li { padding-left: 19px; position: relative; }
  .qualify li::before {
    content: ""; position: absolute; left: 3px; top: 10px;
    width: 5px; height: 5px; background: var(--paper);
  }
  .contact {
    position: absolute;
    left: 31px; top: 704px;
    width: 581px;
    font-size: 20px;
    line-height: 26px;
  }
  .contact h3 { font-size: 20px; font-weight: 700; border-bottom: 2px solid var(--ink); line-height: 27px; }
  .contact .name { border-bottom: 2px solid var(--ink); line-height: 27px; }
  .contact address { font-style: normal; padding-top: 4px; }
  .contact .company { text-transform: none; }
  .contact .company span { text-transform: uppercase; }
  .reach {
    position: absolute;
    left: 0; top: 838px;
    width: 640px; height: 48px;
    background: var(--ink);
    color: var(--paper);
    font-weight: 700;
    font-size: 20px;
    display: flex; align-items: center;
    padding-left: 37px;
    gap: 14px;
  }
  .reach .item { display: flex; align-items: center; gap: 4px; }
  .reach svg { width: 17px; height: 17px; }
</style>
</head>
<body>
  <article class="ad">
    <div class="state-map" role="img" aria-label="Black silhouette map of California"></div>
    <div class="state-map-body" role="img" aria-label="Black silhouette map of California"></div>

    <h1 class="topics">FSMA<br>Production<br>Skills<strong>Worker<br>Safety</strong></h1>
    <div class="topics-bar"></div>

    <p class="pitch">You<br>Do the<br>Training<strong>The State<br>of<br>California<br>Pays<br>for it!</strong></p>

    <section class="qualify">
      <h2>How to qualify:</h2>
      <ul>
        <li>Train California workers only.</li>
        <li>Trainees must earn $15/hour</li>
        <li>Full-time workers only.</li>
        <li>Employees must attend at least 8 hours<br>or training</li>
        <li>You must train 200 or more employees</li>
        <li>Seasonal workers are eligible</li>
      </ul>
    </section>

    <section class="contact">
      <h3>Contact</h3>
      <p class="name">Daniel Marsh</p>
      <address>
        <span class="company"><span>Keystone Learning Company,</span> Inc.,<span>1200 Harbor</span></span><br>
        Crest Drive, Suite 310, Irvine, CA 92614<br>
        www.klgcal.com&nbsp; www.klgfoodsafety.com
      </address>
    </section>

    <footer class="reach">
      <span class="item">
        <svg viewBox="0 0 20 20" aria-hidden="true"><circle cx="10" cy="10" r="8.5" fill="none" stroke="#fff" stroke-width="2"/><rect x="5.5" y="6.5" width="9" height="7" fill="none" stroke="#fff" stroke-width="1.5"/><path d="M5.5 6.5 L10 10.5 L14.5 6.5" fill="none" stroke="#fff" stroke-width="1.5"/></svg>
        dan.marsh@klgcal.com
      </span>
      <span class="item">
        <svg viewBox="0 0 20 20" aria-hidden="true"><circle cx="10" cy="10" r="9" fill="#fff"/><path d="M7 5 L9 7.5 L8 9 Q9 11.5 11 12 L12.5 11 L15 13 L13.5 15 Q8 15 5.5 8 Z" fill="#000"/></svg>
        (555)014-2870
      </span>
    </footer>
  </article>
</body>
</html>
```